KMT Billboard Design Project

Tax sensitization messages. Please find attached document with the creative brief information.

Reason: Submitted designs yet be viewed by project team.

```html
<!DOCTYPE html>
<html lang="en">
<head>
<meta charset="utf-8">
<title>KMT Tax Preparation Billboard</title>
<link rel="stylesheet" href="https://fonts.googleapis.com/css2?family=Anton&family=Roboto:wght@400;500&display=swap">
<style>
  :root {
    --navy: #0b1f66;
    --red: #e8141b;
    --white: #ffffff;
    --ink: #1f2a44;
    --page: #f4f5f7;
    --social-1: #2a9ad8;
    --social-2: #34579a;
    --social-3: #1a80b6;
  }
  html, body {
    margin: 0;
    padding: 0;
    width: 1200px;
    height: 1200px;
    overflow: hidden;
    background: var(--page);
  }
  .canvas {
    position: relative;
    width: 1200px;
    height: 1200px;
  }
  .billboard {
    position: absolute;
    left: 20px;
    top: 332px;
    width: 1160px;
    height: 535px;
    background: var(--white);
    overflow: hidden;
    box-shadow: 0 2px 10px rgba(0,0,0,0.12);
  }
  .billboard-shapes {
    position: absolute;
    inset: 0;
    width: 100%;
    height: 100%;
  }
  .brand {
    position: absolute;
    left: 722px;
    top: 40px;
    width: 228px;
    text-align: center;
    font-family: "Anton", sans-serif;
    font-size: 66px;
    line-height: 1;
    letter-spacing: 4px;
    color: var(--red);
  }
  .headline {
    position: absolute;
    left: 606px;
    top: 172px;
    margin: 0;
    font-family: "Anton", sans-serif;
    font-weight: 400;
    line-height: 1;
    white-space: nowrap;
  }
  .headline-lead {
    display: block;
    font-size: 46px;
    color: var(--navy);
    letter-spacing: 0.2px;
  }
  .headline-main {
    display: block;
    margin-top: 2px;
    font-size: 75px;
    color: var(--red);
  }
  .phone {
    position: absolute;
    left: 770px;
    top: 352px;
    display: flex;
    align-items: center;
    gap: 14px;
    font-family: "Roboto", sans-serif;
    font-weight: 500;
    font-size: 40px;
    color: var(--white);
    letter-spacing: 1px;
    white-space: nowrap;
  }
  .phone svg { width: 38px; height: 38px; }
  .web {
    position: absolute;
    left: 744px;
    top: 478px;
    display: flex;
    align-items: center;
    gap: 10px;
    font-family: "Roboto", sans-serif;
    font-size: 20px;
    color: var(--ink);
    white-space: nowrap;
  }
  .web svg { width: 26px; height: 26px; }
  .social {
    position: absolute;
    left: 975px;
    top: 472px;
    display: flex;
    gap: 14px;
  }
  .social-square {
    width: 34px;
    height: 34px;
    border-radius: 3px;
  }
  .social-square.one { background: var(--social-1); }
  .social-square.two { background: var(--social-2); }
  .social-square.three { background: var(--social-3); }
</style>
</head>
<body>
<main class="canvas">
  <section class="billboard">
    <svg class="billboard-shapes" viewBox="0 0 932 430" preserveAspectRatio="none">
      <defs>
        <linearGradient id="panelFade" x1="0" y1="0" x2="0" y2="1">
          <stop offset="0" stop-color="#e3e6ea"/>
          <stop offset="0.6" stop-color="#f6f7f8"/>
          <stop offset="1" stop-color="#ffffff"/>
        </linearGradient>
        <linearGradient id="photoTone" x1="0" y1="0" x2="1" y2="1">
          <stop offset="0" stop-color="#f3efe6"/>
          <stop offset="0.55" stop-color="#d8b47a"/>
          <stop offset="1" stop-color="#a6763a"/>
        </linearGradient>
      </defs>
      <polygon class="grey-panel" points="376,0 932,0 932,418 480,418" fill="url(#panelFade)"/>
      <rect role="img" aria-label="Photo of an alarm clock beside wooden blocks spelling TAX topped with stacks of coins" x="20" y="105" width="360" height="240" rx="6" fill="url(#photoTone)"/>
      <polygon class="stripe-red" points="313,0 335,0 452,418 425,418" fill="var(--red)"/>
      <polygon class="stripe-navy" points="342,0 376,0 480,418 458,418" fill="var(--navy)"/>
      <rect class="brand-rule" x="580" y="96" width="183" height="2" fill="var(--red)"/>
      <rect class="brand-rule" x="580" y="100" width="183" height="1" fill="var(--navy)"/>
      <polygon class="phone-band-red" points="680,338 932,326 932,362 652,362" fill="var(--red)"/>
      <polygon class="phone-band-navy" points="560,272 932,272 932,326 532,342" fill="var(--navy)"/>
      <rect class="base-navy" x="0" y="418" width="480" height="12" fill="var(--navy)"/>
      <rect class="base-red" x="480" y="418" width="452" height="12" fill="var(--red)"/>
    </svg>

    <div class="brand">KMT</div>

    <h1 class="headline">
      <span class="headline-lead">Relaxed And Experienced</span>
      <span class="headline-main">Tax Preparation</span>
    </h1>

    <div class="phone">
      <svg viewBox="0 0 24 24" aria-hidden="true">
        <path fill="#fff" d="M6.6 3.5l2.6 3.3c.4.5.3 1.2-.1 1.6l-1.4 1.3c.9 2 2.5 3.7 4.6 4.7l1.3-1.4c.4-.4 1.1-.5 1.6-.1l3.3 2.6c.5.4.6 1.1.2 1.6l-1.6 2c-.6.7-1.6 1-2.5.7C8.6 18.2 5.8 15.4 4.200 9.5c-.3-.9 0-1.9.7-2.5l1.7-1.6z"/>
        <path fill="none" stroke="#fff" stroke-width="1.6" stroke-linecap="round" d="M14 3.5a6.5 6.5 0 0 1 6.5 6.5M14 6.8a3.2 3.2 0 0 1 3.2 3.2"/>
      </svg>
      <span>0770456321</span>
    </div>

    <div class="web">
      <svg viewBox="0 0 24 24" aria-hidden="true">
        <g fill="none" stroke="#1f2a44" stroke-width="1.6">
          <circle cx="12" cy="12" r="9.5"/>
          <ellipse cx="12" cy="12" rx="4.2" ry="9.5"/>
          <path d="M2.5 12h19M4 7h16M4 17h16"/>
        </g>
      </svg>
      <span>www.kmtrev.org</span>
    </div>

    <div class="social" aria-label="Social channels">
      <span class="social-square one"></span>
      <span class="social-square two"></span>
      <span class="social-square three"></span>
    </div>
  </section>
</main>
</body>
</html>
```